Real Estate Business Cards

Looking for a clean, sharp and professional look for our Real Estate investment Fund that invests in Multi Family Apartment buildings.

Target Market(s)

Real Estate Fund

Industry/Entity Type

Real Estate

Contact Information for Business Card

Company Description: Real Estate Investment Fund
Company Name: RKW Holdings
Name: Marcus Olvane
Cell: (917) 482-0657
Email: marcus@rkwholdings-example.com
Website: www.rkwholdings-example.com
Address: 418, 9th Street, Brooklyn NY 11218

Colors

Designer to choose colors to be used in the design.

Requirements
Nice to have
• Colors to match logo

```html
<!DOCTYPE html>
<html lang="en">
<head>
<meta charset="utf-8">
<title>RKW Holdings – Business Cards</title>
<link rel="stylesheet" href="https://fonts.googleapis.com/css2?family=Cinzel:wght@400;600&family=EB+Garamond:wght@400;500&display=swap">
<style>
  :root {
    --brand-blue: #0b6ea8;
    --ink: #2b2b2b;
    --paper: #ffffff;
    --backdrop: #e9e6e2;
    --mark-grey: #4a4a4a;
  }
  * { box-sizing: border-box; margin: 0; padding: 0; }
  html, body { width: 1200px; height: 960px; overflow: hidden; }
  body {
    background: var(--backdrop);
    display: flex;
    flex-direction: column;
    align-items: center;
    justify-content: center;
    gap: 50px;
  }
  .card {
    width: 700px;
    height: 400px;
    border-radius: 26px;
    box-shadow: 0 6px 18px rgba(0,0,0,0.18);
    position: relative;
    overflow: hidden;
  }
  .card--front {
    background: var(--brand-blue);
    display: flex;
    align-items: center;
    justify-content: center;
    gap: 22px;
  }
  .brand-square {
    width: 62px;
    height: 62px;
    border: 6px solid var(--paper);
    border-radius: 3px;
  }
  .brand-name {
    font-family: "Cinzel", serif;
    font-weight: 400;
    letter-spacing: 2px;
  }
  .card--front .brand-name { color: var(--paper); font-size: 40px; }

  .card--back {
    background: var(--paper);
    display: flex;
    align-items: center;
    padding: 0 40px 0 60px;
  }
  .back-brand {
    width: 300px;
    display: flex;
    flex-direction: column;
    align-items: center;
    gap: 26px;
  }
  .back-brand .brand-square {
    width: 90px;
    height: 90px;
    border: 10px solid var(--brand-blue);
  }
  .back-brand .brand-name { color: var(--brand-blue); font-size: 34px; }
  .divider {
    width: 2px;
    height: 250px;
    background: var(--brand-blue);
    margin: 0 28px 0 20px;
  }
  .contact { font-family: "EB Garamond", serif; color: var(--ink); }
  .contact__name {
    font-family: "Cinzel", serif;
    font-weight: 600;
    color: var(--brand-blue);
    font-size: 30px;
    letter-spacing: 1px;
    line-height: 1.1;
  }
  .contact__role { font-size: 21px; margin-bottom: 6px; }
  .contact__line { font-size: 20px; line-height: 1.3; }
  .contact__item {
    display: flex;
    align-items: center;
    gap: 10px;
    font-size: 19px;
    line-height: 1.4;
  }
  .contact__item svg { width: 14px; height: 14px; flex: none; fill: var(--brand-blue); }
</style>
</head>
<body>
  <section class="card card--front" aria-label="Card front">
    <span class="brand-square" aria-hidden="true"></span>
    <span class="brand-name">RKW HOLDINGS</span>
  </section>

  <section class="card card--back" aria-label="Card back">
    <div class="back-brand">
      <span class="brand-square" aria-hidden="true"></span>
      <span class="brand-name">RKW HOLDINGS</span>
    </div>
    <div class="divider"></div>
    <div class="contact">
      <div class="contact__name">MARCUS OLVANE</div>
      <div class="contact__role">Owner</div>
      <div class="contact__line">418, 9th Street,</div>
      <div class="contact__line">Brooklyn NY 11218</div>
      <div class="contact__item">
        <svg viewBox="0 0 24 24" aria-hidden="true"><path d="M6.6 10.8a15.1 15.1 0 006.6 6.6l2.2-2.2a1 1 0 011-.25 11.4 11.4 0 003.6.57 1 1 0 011 1V20a1 1 0 01-1 1A17 17 0 013 4a1 1 0 011-1h3.5a1 1 0 011 1 11.4 11.4 0 00.57 3.6 1 1 0 01-.25 1z"/></svg>
        (917) 482-0657
      </div>
      <div class="contact__item">
        <svg viewBox="0 0 24 24" aria-hidden="true"><path d="M2 5h20v14H2z M2 5l10 8 10-8" stroke="#fff" stroke-width="1.5"/></svg>
        marcus@rkwholdings-example.com
      </div>
      <div class="contact__item">
        <svg viewBox="0 0 24 24" aria-hidden="true"><circle cx="12" cy="12" r="10"/></svg>
        www.rkwholdings-example.com
      </div>
    </div>
  </section>
</body>
</html>
```